B2B Umbrella Site Requires Simple, Stylish Slider Designs

We're a dynamic promotional merchandise business in the process of building a new B2B Umbrella Store. It's our goal to provide printed umbrellas to suit the needs of our clients. Our main page is in need of ONE large key banner and THREE smaller sub category banners. We would like to see designs that use grey and green (or similar) to match with the theme of our layout. See: http://canopyharbor.com.au/

The final designs should convey the desirability of our umbrellas while looking slick and modern in style. Please find attached our place holder banners for size reference and umbrella images to use in designs. If you require any further details or content, feel free to contact us.

Target Market(s)

Professionals and businesses across a wide range of fields. We offer a customisable product so we are as flexible as our target market.

Industry/Entity Type

Building

Font styles to use
Sans Serif

Requirements
Must have
• Must match sizes of attached sample graphics (
sub_banner + main_banner images). Must feature umbrella images attached to the brief - pick which images suit your design, but please ensure they are the correct umbrella style for the banner text. Clear, stylish text based on existing text found on sample graphics.
Nice to have
• Colours similar to the ones existing on the website already.
Should not have
• No serif fonts or clipart. Colours that do not facilitate easy reading.

```html
<!DOCTYPE html>
<html lang="en">
<head>
<meta charset="utf-8">
<title>Medium Corporate Umbrellas Banner</title>
<link rel="stylesheet" href="https://fonts.googleapis.com/css2?family=Open+Sans:wght@400;600&display=swap">
<style>
  :root {
    --page-white: #ffffff;
    --panel-light: #f4f5f7;
    --panel-mid: #dcdee2;
    --panel-edge: #c9ccd1;
    --ribbon-green-light: #8fd14a;
    --ribbon-green: #5db62f;
    --ribbon-green-dark: #3f9a1f;
    --ribbon-fold: #1f1f1f;
    --text-white: #ffffff;
    --text-yellow: #f4ee1a;
    --canopy-light: #b0442e;
    --canopy-mid: #8e2e1f;
    --canopy-dark: #5e1a12;
  }
  html, body {
    margin: 0;
    padding: 0;
    overflow: hidden;
    background: var(--page-white);
  }
  .banner {
    position: relative;
    width: 1200px;
    height: 653px;
    overflow: hidden;
    background: var(--page-white);
    font-family: "Open Sans", sans-serif;
  }
  .banner__panel {
    position: absolute;
    left: 40px;
    top: 36px;
    width: 1160px;
    height: 617px;
    background: radial-gradient(ellipse at 52% 50%, var(--panel-light) 0%, var(--panel-mid) 70%, var(--panel-edge) 100%);
  }
  .banner__product {
    position: absolute;
    left: 666px;
    top: 72px;
    width: 468px;
    height: 528px;
    border-radius: 48% 52% 40% 44% / 40% 38% 56% 58%;
    background: radial-gradient(ellipse at 40% 30%, var(--canopy-light) 0%, var(--canopy-mid) 55%, var(--canopy-dark) 100%);
    transform: rotate(-8deg);
    filter: drop-shadow(12px 14px 10px rgba(0,0,0,0.25));
  }
  .banner__ribbon {
    position: absolute;
    left: 0;
    top: 0;
    width: 1200px;
    height: 653px;
  }
  .ribbon__title {
    font-family: "Open Sans", sans-serif;
    font-weight: 400;
    fill: var(--text-white);
    text-anchor: middle;
  }
  .ribbon__title--accent {
    fill: var(--text-yellow);
  }
</style>
</head>
<body>
<div class="banner">
  <div class="banner__panel"></div>
  <div class="banner__product" role="img" aria-label="Photo of an open rust-red corporate umbrella with a curved wooden handle"></div>

  <svg class="banner__ribbon" viewBox="0 0 1200 653" aria-hidden="false">
    <defs>
      <linearGradient id="ribbonFill" x1="0" y1="0" x2="1" y2="1">
        <stop offset="0" stop-color="var(--ribbon-green-light)"/>
        <stop offset="0.55" stop-color="var(--ribbon-green)"/>
        <stop offset="1" stop-color="var(--ribbon-green-dark)"/>
      </linearGradient>
    </defs>
    <polygon class="ribbon__fold" points="518,10 552,10 578,36 492,36" fill="var(--ribbon-fold)"/>
    <polygon class="ribbon__fold" points="10,518 10,552 36,578 36,492" fill="var(--ribbon-fold)"/>
    <path class="ribbon__band" d="M296,10 L532,10 L10,532 L10,296 Q10,286 18,278 L278,18 Q286,10 296,10 Z" fill="url(#ribbonFill)"/>
    <text class="ribbon__title" font-size="44" letter-spacing="1" transform="translate(190,202) rotate(-45)">MEDIUM <tspan class="ribbon__title--accent">CORPORATE</tspan></text>
    <text class="ribbon__title" font-size="50" letter-spacing="2" transform="translate(252,252) rotate(-45)">UMBRELLAS</text>
  </svg>
</div>
</body>
</html>
```